Brindle Grass Services website design

We want to create a Sports turf website for our business Brindle Grass Services - we do sports turf management on sports fields around the Mackay region soccer rugby league softball fields etc from full turf management plans and maintenance to just supply and apply of turf management products and just supply of products with program we also do grounds facility maintenance at council facility's and grounds that require a higher level of care - we will up load our logos and fonts etc to assist with the colour pallet for the website - we will have to have a landing page a shop page with tabs a gallery tab along with a grants initiative and our coastals finest green tab also - our font for the txt is called ethnocentric
Updates

how do we open time for people to submit we have no one submitted

Industry/Entity Type

Turf

Coding

Coded - Design and coding required

Number of Pages Required

5+ page

Font styles to use
Other font styles liked:
• ethnocentric

Requirements
Must have
• I have mentioned some waffle in the description that should assist
Should not have
• anything not related

```html
<!DOCTYPE html>
<html lang="en">
<head>
<meta charset="utf-8">
<title>Brindle Grass Services — Elite Sports Turf Mackay</title>
<link href="https://fonts.googleapis.com/css2?family=Orbitron:wght@700;800;900&family=Montserrat:wght@400;500;600;700&family=Inter:wght@400;500;600;700&display=swap" rel="stylesheet">
<style>
:root{
  --green:#22b14c;
  --green-dark:#0b8a3a;
  --green-bright:#3ecf5e;
  --black:#000;
  --panel:#0f1411;
  --panel-line:#1e2620;
  --footer:#0c120e;
  --white:#fff;
  --muted:#c9cfca;
}
*{margin:0;padding:0;box-sizing:border-box}
html,body{width:953px;height:1200px;overflow:hidden;background:var(--black)}
body{position:relative;font-family:"Inter",sans-serif;color:var(--white)}
.display{font-family:"Orbitron",sans-serif;font-weight:900;letter-spacing:.04em;text-transform:uppercase}

/* hero */
.hero{position:absolute;left:0;top:0;width:953px;height:520px;overflow:hidden}
.hero-photo{position:absolute;inset:0;background:linear-gradient(180deg,#2a4a72 0%,#3d5d7a 22%,#3b5a3f 38%,#2f5a36 60%,#1e3a26 85%,#14241a 100%)}
.hero-shade{position:absolute;inset:0;background:rgba(8,18,28,.35)}
.site-header{position:absolute;left:0;top:0;width:953px;height:60px}
.brand{position:absolute;left:10px;top:14px;display:flex;align-items:center;gap:7px;font-family:"Montserrat",sans-serif;font-weight:700;font-size:17px;letter-spacing:.02em;color:var(--white)}
.brand .dot{width:10px;height:10px;border-radius:50%;background:var(--green)}
.main-nav{position:absolute;right:14px;top:14px;display:flex;align-items:center;gap:19px;font-family:"Montserrat",sans-serif;font-size:9px;font-weight:500;text-transform:uppercase}
.main-nav a{color:var(--white);text-decoration:none;position:relative}
.main-nav a.active{font-weight:700}
.main-nav a.active::after{content:"";position:absolute;left:0;right:0;bottom:-5px;height:2px;background:var(--green)}
.main-nav a.nav-contact{border:1px solid var(--white);padding:5px 9px}

.hero-panel{position:absolute;left:0;top:160px;width:600px;height:190px}
.hero-frame{position:absolute;left:0;top:0}
.hero-tag{position:absolute;left:103px;top:4px;height:22px;width:211px;background:var(--green);clip-path:polygon(7% 0,100% 0,94% 100%,0 100%);font-family:"Orbitron",sans-serif;font-weight:800;font-size:8.5px;letter-spacing:.06em;display:flex;align-items:center;padding-left:16px;text-transform:uppercase;white-space:nowrap}
.hero-title{position:absolute;left:105px;top:34px;font-size:33px;line-height:35px;white-space:nowrap}
.hero-title .line-one{padding-left:14px}
.hero-title .drop{display:inline-block;width:13px;height:20px;margin:0 9px}
.hero-lede{position:absolute;left:91px;top:111px;width:400px;font-family:"Montserrat",sans-serif;font-size:10.8px;line-height:14.5px}
.hero-ctas{position:absolute;left:85px;top:154px;display:flex}
.btn-slant{height:24px;display:flex;align-items:center;justify-content:center;font-family:"Montserrat",sans-serif;font-weight:700;font-size:8.5px;text-transform:uppercase;color:var(--white);text-decoration:none;white-space:nowrap}
.btn-shop{width:128px;background:var(--green-dark);clip-path:polygon(0 0,100% 0,92% 100%,8% 100%)}
.btn-programs{width:128px;background:var(--green);clip-path:polygon(8% 0,100% 0,92% 100%,0 100%);margin-left:-6px}

/* content */
.content{position:absolute;left:0;top:520px;width:953px;height:504px;background:radial-gradient(ellipse 70px 160px at 0 230px,rgba(30,140,60,.35),transparent),radial-gradient(ellipse 80px 200px at 953px 300px,rgba(30,140,60,.35),transparent),var(--black)}
.stats{position:absolute;left:129px;top:50px;display:grid;grid-template-columns:repeat(4,164px);gap:12px}
.stat{height:61px;background:var(--panel);border:1px solid var(--panel-line);padding:15px 16px}
.stat-label{font-size:7.5px;color:var(--muted);display:flex;align-items:center;gap:4px}
.stat-icon{width:7px;height:7px}
.stat-value{font-size:12.5px;font-weight:700;margin-top:5px}
.section-title{position:absolute;left:129px;top:162px;font-size:15px}
.section-lede{position:absolute;left:129px;top:186px;width:340px;font-size:7.5px;line-height:10px}
.programs{position:absolute;left:129px;top:208px;display:grid;grid-template-columns:repeat(3,224px);gap:12px}
.card{background:var(--panel);border:1px solid var(--panel-line);padding:16px 15px}
.program{height:96px}
.card-title{font-family:"Orbitron",sans-serif;font-weight:900;font-size:8px;letter-spacing:.08em;text-transform:uppercase}
.card-text{font-size:7.5px;line-height:9.6px;color:var(--muted);margin-top:9px}
.price{font-size:7.5px;font-weight:700;margin-top:8px}
.services{position:absolute;left:129px;top:357px;display:grid;grid-template-columns:repeat(2,342px);gap:12px}
.service{height:102px}
.btn{display:inline-block;margin-top:9px;font-size:7.5px;font-weight:600;color:var(--white);text-decoration:none;padding:6px 9px}
.btn-solid{background:var(--green)}
.btn-outline{border:1px solid var(--green)}

/* footer */
.site-footer{position:absolute;left:0;top:1024px;width:953px;height:176px;background:var(--footer);border-top:1px solid var(--panel-line)}
.footer-rule{position:absolute;left:129px;right:129px;top:17px;height:1px;background:var(--panel-line)}
.footer-brand{position:absolute;left:129px;top:35px;width:165px}
.footer-name{font-family:"Montserrat",sans-serif;font-weight:700;font-size:10px;display:flex;align-items:center;gap:5px}
.footer-name .dot{width:7px;height:7px;border-radius:50%;background:var(--green)}
.footer-about{font-size:7px;line-height:9.5px;color:var(--muted);margin-top:9px}
.region-pill{display:inline-block;margin-top:6px;background:var(--green-bright);color:#06210f;border-radius:8px;font-family:"Orbitron",sans-serif;font-weight:800;font-size:5px;letter-spacing:.08em;padding:3px 6px;text-transform:uppercase}
.footer-col{position:absolute;top:38px}
.footer-col h4{font-size:9px;font-weight:700}
.footer-col ul{list-style:none;margin-top:6px;padding-left:6px}
.footer-col li{font-size:7.5px;color:var(--muted);height:30px;line-height:14px}
.copyright{position:absolute;left:129px;top:160px;font-size:6.5px;color:var(--muted)}
</style>
</head>
<body>

<section class="hero">
  <div class="hero-photo" role="img" aria-label="Aerial photograph of a floodlit rugby league stadium pitch in Mackay"></div>
  <div class="hero-shade"></div>

  <header class="site-header">
    <div class="brand"><span class="dot"></span>Brindle Grass Services</div>
    <nav class="main-nav">
      <a class="active" href="#">Home</a>
      <a href="#">Shop</a>
      <a href="#">Gallery</a>
      <a href="#">Grants</a>
      <a href="#">Coastal’s Finest Green</a>
      <a href="#">About</a>
      <a class="nav-contact" href="#">Contact</a>
    </nav>
  </header>

  <div class="hero-panel">
    <svg class="hero-frame" width="600" height="190" viewBox="0 0 600 190" aria-hidden="true">
      <polygon points="112,9 557,9 500,154 51,154" fill="rgba(10,16,14,.72)"/>
      <polyline points="312,9 557,9 489,166 325,166" fill="none" stroke="#fff" stroke-width="1"/>
    </svg>
    <div class="hero-tag">Sports Turf Specialists</div>
    <h1 class="hero-title display"><span class="line-one">Elite Sports</span><br>Turf<svg class="drop" viewBox="0 0 12 18"><path d="M6 0 C6 5 0 9 0 12.5 A6 5.5 0 0 0 12 12.5 C12 9 6 5 6 0Z" fill="#1fa3e0"/></svg>Mackay</h1>
    <p class="hero-lede">From full management plans to supply &amp; apply, we keep soccer, rugby league and softball surfaces game-ready—safe, fast and consistent.</p>
    <div class="hero-ctas">
      <a class="btn-slant btn-shop" href="#">Shop Products</a>
      <a class="btn-slant btn-programs" href="#">View Programs</a>
    </div>
  </div>
</section>

<main class="content">
  <div class="stats">
    <div class="stat"><div class="stat-label"><svg class="stat-icon" viewBox="0 0 8 8"><circle cx="4" cy="4" r="4" fill="#22b14c"/></svg>Surfaces managed</div><div class="stat-value">40+ fields</div></div>
    <div class="stat"><div class="stat-label"><svg class="stat-icon" viewBox="0 0 8 8"><circle cx="4" cy="3" r="2.5" fill="#e23b3b"/><line x1="4" y1="5" x2="4" y2="8" stroke="#aaa"/></svg>Service area</div><div class="stat-value">Mackay</div></div>
    <div class="stat"><div class="stat-label"><svg class="stat-icon" viewBox="0 0 8 8"><circle cx="4" cy="4.5" r="3.3" fill="#ddd"/></svg>Turnaround</div><div class="stat-value">Fast</div></div>
    <div class="stat"><div class="stat-label"><svg class="stat-icon" viewBox="0 0 10 10"><polygon points="5,0 6.2,3.6 10,3.7 7,6 8.1,9.6 5,7.5 1.9,9.6 3,6 0,3.7 3.8,3.6" fill="#f5c518"/></svg>Rating</div><div class="stat-value">5.0</div></div>
  </div>

  <h2 class="section-title display">Turf Management Programs</h2>
  <p class="section-lede">Pick a program that fits your facility—each includes a season-ready plan, site visits, and supply &amp; apply of products as required.</p>

  <div class="programs">
    <article class="card program"><h3 class="card-title">Essential Care</h3><p class="card-text">Monthly visits • Mowing specs • Nutrient program • Wetting agents • Broadleaf &amp; bindii control.</p><p class="price">$</p></article>
    <article class="card program"><h3 class="card-title">Performance</h3><p class="card-text">Fortnightly visits • Renovations • In-season recovery • Pest &amp; disease monitoring • Detailed reporting.</p><p class="price">$$</p></article>
    <article class="card program"><h3 class="card-title">Elite</h3><p class="card-text">Weekly visits • Growth regulation • Sand topdressing • Full renovation plan • Match-day presentation.</p><p class="price">$$$</p></article>
  </div>

  <div class="services">
    <article class="card service"><h3 class="card-title">Facility Maintenance</h3><p class="card-text">Beyond the grass: line marking, irrigation checks, litter &amp; debris removal, safety checks and council-level presentation.</p><a class="btn btn-solid" href="#">Request a Site Visit</a></article>
    <article class="card service"><h3 class="card-title">Supply &amp; Apply</h3><p class="card-text">We can supply products with an endorsed program—or apply them for you. Bulk rates available for clubs and councils.</p><a class="btn btn-outline" href="#">Browse Products</a></article>
  </div>
</main>

<footer class="site-footer">
  <div class="footer-rule"></div>
  <div class="footer-brand">
    <div class="footer-name"><span class="dot"></span>Brindle Grass Services</div>
    <p class="footer-about">Sports turf management for clubs, schools and councils across Mackay: full programs, supply &amp; apply, and facility care.</p>
    <span class="region-pill">QLD • Mackay Region</span>
  </div>
  <div class="footer-col" style="left:306px"><h4>Company</h4><ul><li>About</li><li>Gallery</li><li>Grants</li></ul></div>
  <div class="footer-col" style="left:483px"><h4>Services</h4><ul><li>Turf Programs</li><li>Facility Maintenance</li><li>Shop</li></ul></div>
  <div class="footer-col" style="left:660px"><h4>Contact</h4><ul><li>Contact Form</li><li>hello@brindlegrass.example</li><li>Social Page</li></ul></div>
  <p class="copyright">© 2025 Brindle Grass Services. All rights reserved.</p>
</footer>

</body>
</html>
```